Media Banner

Create a banner similar to the one in the link below showing the various media publications (TVQRN, Marlowby Ledger, Kite Wire, Pellanstroud Bulletin) and then link to "More News..."

https://www.loanvistra.com/

The bar on loan vistra is blue. Please make this bar organe to match this site:
www.bramfieldlegal.com
The bar will be used on this cite to run accross the page.

Industry/Entity Type

Graphic Design

```html
<!DOCTYPE html>
<html lang="en">
<head>
<meta charset="utf-8">
<title>Media Banner</title>
<link rel="stylesheet" href="https://fonts.googleapis.com/css2?family=Arimo:wght@400;700&display=swap">
<style>
  :root {
    --page-bg: #ffffff;
    --bar-orange: #ca7200;
    --bar-text: #ffffff;
  }
  * { box-sizing: border-box; margin: 0; padding: 0; }
  html, body {
    width: 1200px;
    height: 1200px;
    overflow: hidden;
    background: var(--page-bg);
  }
  .canvas {
    position: relative;
    width: 1200px;
    height: 1200px;
  }
  .media-bar {
    position: absolute;
    left: 15px;
    top: 476px;
    width: 1175px;
    height: 199px;
    background: var(--bar-orange);
    display: flex;
    align-items: center;
    justify-content: space-between;
    padding: 0 18px 0 18px;
    color: var(--bar-text);
    font-family: "Arimo", Arial, sans-serif;
  }
  .seen-label {
    font-size: 22px;
    font-weight: 400;
    white-space: nowrap;
  }
  .outlet {
    display: flex;
    align-items: center;
    gap: 8px;
    font-weight: 400;
    white-space: nowrap;
    color: var(--bar-text);
    text-decoration: none;
  }
  .outlet-dot {
    width: 22px;
    height: 22px;
    border-radius: 50%;
    background: var(--bar-text);
    flex: none;
  }
  .outlet--tvqrn { font-size: 32px; letter-spacing: -0.5px; }
  .outlet--ledger { font-size: 26px; letter-spacing: 1px; text-transform: uppercase; }
  .outlet--kite { font-size: 28px; }
  .outlet--bulletin { font-size: 28px; }
  .more-news {
    font-size: 22px;
    color: var(--bar-text);
    text-decoration: none;
    white-space: nowrap;
  }
</style>
</head>
<body>
<div class="canvas">
  <nav class="media-bar" aria-label="As seen in">
    <span class="seen-label">As Seen In:</span>
    <span class="outlet outlet--tvqrn"><span class="outlet-dot"></span>TVQRN</span>
    <span class="outlet outlet--ledger">Marlowby Ledger</span>
    <span class="outlet outlet--kite">Kite Wire</span>
    <span class="outlet outlet--bulletin">Pellanstroud Bulletin</span>
    <a class="more-news" href="https://www.loanvistra.com/">More News...</a>
  </nav>
</div>
</body>
</html>
```